Lawn mowing business card design

We need a business card design for our lawn mowing and gardening business which is located in the Northern Beaches of Sydney. Our business name is Meadowline Turf and our logo is predominantly green and yellow in color. Please see our website at www.meadowlineturf.com.au for design ideas. The business targets young professionals and older clientele. As such the font should be easy to read, but I also want the business card to be colorful and stand out.

Target Market(s)

young professionals

Industry/Entity Type

Lawn Care

Contact Information for Business Card

Meadowline Turf, Gareth Pellow, 0478559201, www.meadowlineturf.com.au, email: meadowlineturf@mailbox-example.com

Font styles to use
Serif

Colors
9bcb3b
fbed22

Requirements
Must have
• Must include the details listed above. Must include the attached logo.
Nice to have
• Logo attached with two copies. The logo without any writing is high quality, please feel free to be creative with the text stating our business name "Meadowline Turf" using this file.

```html
<!DOCTYPE html>
<html lang="en">
<head>
<meta charset="utf-8">
<title>Meadowline Turf – Business Card</title>
<link rel="stylesheet" href="https://fonts.googleapis.com/css2?family=Open+Sans:wght@300;400;600&family=Noto+Serif:wght@400&display=swap">
<style>
  :root {
    --page-bg: #ece9e4;
    --card-white: #ffffff;
    --card-shade: #ececec;
    --lime: #9bcb3b;
    --lime-deep: #7fb52a;
    --sun: #fbed22;
    --ink: #1f1f1f;
    --ink-soft: #4a4a4a;
    --rule: #8a8a8a;
  }
  * { margin: 0; padding: 0; box-sizing: border-box; }
  html, body { width: 1200px; height: 780px; overflow: hidden; }
  body {
    background: var(--page-bg);
    font-family: "Open Sans", Arial, sans-serif;
    color: var(--ink);
    position: relative;
  }
  .card {
    position: absolute;
    top: 240px;
    width: 520px;
    height: 300px;
    border-radius: 18px;
    background: radial-gradient(ellipse at 55% 40%, var(--card-white) 0%, var(--card-white) 45%, var(--card-shade) 100%);
    box-shadow: 0 2px 0 #d6d6d6, 0 4px 0 #e8e8e8, 0 6px 0 #d2d2d2, 0 14px 28px rgba(0,0,0,0.18);
    overflow: hidden;
  }
  .card--front { left: 60px; }
  .card--back { left: 620px; }

  /* brand mark: name with one plain circle */
  .brand-mark {
    position: absolute;
    display: flex;
    flex-direction: column;
    align-items: center;
    gap: 10px;
  }
  .brand-mark__dot {
    width: 74px;
    height: 74px;
    border-radius: 50%;
    background: var(--sun);
  }
  .brand-mark__name {
    font-family: "Open Sans", Arial, sans-serif;
    font-weight: 600;
    font-size: 17px;
    color: var(--lime-deep);
    white-space: nowrap;
  }
  .card--front .brand-mark { left: 16px; top: 96px; width: 160px; }

  .divider {
    position: absolute;
    left: 188px;
    top: 34px;
    width: 1px;
    height: 238px;
    background: var(--rule);
  }
  .details {
    position: absolute;
    left: 204px;
    top: 34px;
    right: 18px;
  }
  .details__company {
    font-weight: 300;
    font-size: 27px;
    letter-spacing: 0.5px;
    color: var(--lime);
    line-height: 1;
    white-space: nowrap;
  }
  .details__tagline {
    font-weight: 400;
    font-size: 13px;
    color: var(--ink-soft);
    margin-top: 3px;
  }
  .details__name {
    font-weight: 400;
    font-size: 30px;
    color: var(--ink);
    margin-top: 24px;
    line-height: 1;
  }
  .contact-list { list-style: none; margin-top: 20px; }
  .contact-list__item {
    display: flex;
    align-items: center;
    gap: 8px;
    font-size: 14px;
    color: var(--ink);
    margin-bottom: 6px;
    white-space: nowrap;
  }
  .contact-list__icon {
    width: 16px;
    height: 16px;
    border-radius: 3px;
    background: var(--lime);
    display: flex;
    align-items: center;
    justify-content: center;
    flex: none;
  }
  .details__web {
    font-family: "Noto Serif", Georgia, serif;
    font-size: 13px;
    color: var(--lime);
    margin-top: 6px;
  }

  /* back */
  .card--back .brand-mark { left: 0; right: 0; top: 60px; }
  .band {
    position: absolute;
    left: 0;
    right: 0;
    bottom: 26px;
    height: 34px;
    background: linear-gradient(90deg, var(--lime-deep), var(--lime));
    display: flex;
    align-items: center;
    justify-content: center;
  }
  .band__web {
    font-family: "Noto Serif", Georgia, serif;
    font-size: 14px;
    color: #2f3a14;
    letter-spacing: 0.3px;
  }
</style>
</head>
<body>
  <section class="card card--front" aria-label="Business card front">
    <div class="brand-mark">
      <span class="brand-mark__dot" aria-hidden="true"></span>
      <span class="brand-mark__name">Meadowline Turf</span>
    </div>
    <div class="divider"></div>
    <div class="details">
      <div class="details__company">MEADOWLINE TURF</div>
      <div class="details__tagline">Lawns and Garden Maintenance</div>
      <div class="details__name">Gareth Pellow</div>
      <ul class="contact-list">
        <li class="contact-list__item">
          <span class="contact-list__icon">
            <svg width="10" height="10" viewBox="0 0 10 10" aria-hidden="true"><path d="M2 1 L4 1 L4.6 3 L3.5 3.8 Q4.5 5.8 6.2 6.5 L7 5.4 L9 6 L9 8 Q8.5 9 7.5 9 Q1 8 1 2 Q1 1 2 1 Z" fill="#1f1f1f"/></svg>
          </span>
          0478559201
        </li>
        <li class="contact-list__item">
          <span class="contact-list__icon">
            <svg width="10" height="10" viewBox="0 0 10 10" aria-hidden="true"><rect x="1" y="2.5" width="8" height="5.5" fill="none" stroke="#1f1f1f" stroke-width="1"/><path d="M1 2.5 L5 5.8 L9 2.5" fill="none" stroke="#1f1f1f" stroke-width="1"/></svg>
          </span>
          meadowlineturf@mailbox-example.com
        </li>
      </ul>
      <div class="details__web">www.meadowlineturf.com.au</div>
    </div>
  </section>

  <section class="card card--back" aria-label="Business card back">
    <div class="brand-mark">
      <span class="brand-mark__dot" aria-hidden="true"></span>
      <span class="brand-mark__name">Meadowline Turf</span>
    </div>
    <div class="band">
      <span class="band__web">www.meadowlineturf.com.au</span>
    </div>
  </section>
</body>
</html>
```